Business Card Design for Engineering Firm

Need a business card design for small mechanical and plumbing engineering form based in Utah. Design should be customizable for all employees.

```html
<!DOCTYPE html>
<html lang="en">
<head>
<meta charset="utf-8">
<title>Harlow Engineering – Business Card</title>
<link rel="stylesheet" href="https://fonts.googleapis.com/css2?family=Montserrat:wght@400;500;700&display=swap">
<style>
  :root {
    --brand-red: #8c1a17;
    --brand-red-dark: #6f1310;
    --ink: #3a3a3a;
    --ink-soft: #5a5a5a;
    --rule: #9a9a9a;
    --paper: #ffffff;
    --backdrop: #e4e5e7;
  }
  * { box-sizing: border-box; margin: 0; padding: 0; }
  html, body {
    width: 1200px; height: 900px; overflow: hidden;
    background: var(--backdrop);
    font-family: "Montserrat", Arial, sans-serif;
  }
  .canvas {
    position: relative; width: 1200px; height: 900px;
  }
  .card {
    position: absolute; left: 320px; width: 560px; height: 320px;
    box-shadow: 0 6px 18px rgba(0,0,0,0.18);
    overflow: hidden;
  }
  .card--front { top: 100px; background: var(--paper); }
  .card--back {
    top: 480px;
    background: linear-gradient(135deg, var(--brand-red) 0%, var(--brand-red-dark) 100%);
    display: flex; align-items: center; justify-content: center;
  }

  /* Front */
  .front__edge {
    position: absolute; left: 0; top: 0; bottom: 0; width: 14px;
    background: var(--brand-red);
  }
  .front__brand {
    position: absolute; left: 44px; top: 0; bottom: 0; width: 220px;
    display: flex; align-items: center; gap: 10px;
  }
  .brand-mark {
    width: 14px; height: 14px; flex: none;
    background: var(--brand-red);
  }
  .brand-name {
    font-weight: 700; font-size: 17px; letter-spacing: 0.6px;
    color: var(--brand-red); line-height: 1.2;
  }
  .front__divider {
    position: absolute; left: 272px; top: 60px; bottom: 60px;
    width: 1px; background: var(--rule);
  }
  .front__details {
    position: absolute; left: 300px; top: 62px; right: 24px;
    color: var(--ink); font-size: 12.5px; line-height: 1.45;
  }
  .person__name {
    font-weight: 700; font-size: 19px; letter-spacing: 0.5px;
    color: var(--brand-red); text-transform: uppercase;
  }
  .person__title { color: var(--ink-soft); margin-bottom: 10px; }
  .address { margin-bottom: 10px; }
  .contact-list { list-style: none; }
  .contact-list li { display: flex; align-items: center; gap: 7px; }
  .contact-list svg { width: 11px; height: 11px; flex: none; fill: var(--brand-red); }

  /* Back */
  .back__brand { display: flex; align-items: center; gap: 18px; }
  .back__brand .brand-mark { width: 22px; height: 22px; background: var(--paper); }
  .back__rule { width: 1px; height: 70px; background: rgba(255,255,255,0.85); }
  .back__brand .brand-name { color: var(--paper); font-size: 26px; letter-spacing: 1px; }
</style>
</head>
<body>
<main class="canvas">

  <section class="card card--front" aria-label="Business card front">
    <div class="front__edge"></div>
    <div class="front__brand">
      <span class="brand-mark"></span>
      <span class="brand-name">HARLOW ENGINEERING</span>
    </div>
    <div class="front__divider"></div>
    <div class="front__details">
      <p class="person__name">Dana Whitfield</p>
      <p class="person__title">CEO/Founder</p>
      <p class="address">418 Canyon Road<br>Provo, UT 84601</p>
      <ul class="contact-list">
        <li>
          <svg viewBox="0 0 24 24" aria-hidden="true"><path d="M6.6 10.8a15 15 0 0 0 6.6 6.6l2.2-2.2a1 1 0 0 1 1-.25 11.4 11.4 0 0 0 3.6.6 1 1 0 0 1 1 1V20a1 1 0 0 1-1 1A17 17 0 0 1 3 4a1 1 0 0 1 1-1h3.5a1 1 0 0 1 1 1c0 1.25.2 2.45.6 3.6a1 1 0 0 1-.25 1z"/></svg>
          555-201-4830
        </li>
        <li>
          <svg viewBox="0 0 24 24" aria-hidden="true"><path d="M7 1h10a2 2 0 0 1 2 2v18a2 2 0 0 1-2 2H7a2 2 0 0 1-2-2V3a2 2 0 0 1 2-2zm0 3v14h10V4zm5 15.5a1.2 1.2 0 1 0 0 2.4 1.2 1.2 0 0 0 0-2.4z"/></svg>
          555-718-2964
        </li>
        <li>
          <svg viewBox="0 0 24 24" aria-hidden="true"><path d="M2 5h20v14H2zm2 2v.5l8 5 8-5V7zm0 2.8V17h16V9.8l-8 5z"/></svg>
          info@harlowengineering.com
        </li>
        <li>
          <svg viewBox="0 0 24 24" aria-hidden="true"><path d="M12 2a10 10 0 1 0 0 20 10 10 0 0 0 0-20zm0 2c.9 0 2.2 1.9 2.7 5H9.3C9.8 5.9 11.1 4 12 4zM4.3 11h3c0-.7.1-1.4.2-2H5a8 8 0 0 0-.7 2zm0 2a8 8 0 0 0 .7 2h2.5a14 14 0 0 1-.2-2zm5 0c.1.7.1 1.4.2 2h5c.1-.6.2-1.3.2-2zm0-2h5.4c0-.7-.1-1.4-.2-2h-5c-.1.6-.2 1.3-.2 2zm7.4 0h3a8 8 0 0 0-.7-2h-2.5c.1.6.2 1.3.2 2zm0 2c0 .7-.1 1.4-.2 2H19a8 8 0 0 0 .7-2zM12 20c-.9 0-2.2-1.9-2.7-5h5.4c-.5 3.1-1.8 5-2.7 5z"/></svg>
          www.harlowengineering.com
        </li>
      </ul>
    </div>
  </section>

  <section class="card card--back" aria-label="Business card back">
    <div class="back__brand">
      <span class="brand-mark"></span>
      <span class="back__rule"></span>
      <span class="brand-name">HARLOW ENGINEERING</span>
    </div>
  </section>

</main>
</body>
</html>
```